Business Card Design for New Game Studio

We need a business card design. We are a new company developing innovative mobile and platform games.

I would like to see very innovative design thats brings out the company's goal and direction.

My Company's goal and direction is to "Evolve the way of gaming, Bring fun and entertainment to all gamers"

Please do use our company logo which I have attached to be included in the design.

Please put in details for name, title, contacts etc ... be creative !!!

Reason: Company logo redesign. Awaiting it. Thanks

Hi all Please do wait for my updated company logo. Thanks

Reason: Still waiting on new company logo. Thanks all

Hi All Designers .... Sorry for the long wait... Please see the new file for my new company logo uploaded. Waiting to see all your creative design. Cheers

Hi All .... Please do not just mass send a whole bunch of similar designs .... Would like to see quality instead of quantity Cheers

Industry/Entity Type

Entertainment

```html
<!DOCTYPE html>
<html lang="en">
<head>
<meta charset="utf-8">
<title>Ascend Kingdoms — Business Card</title>
<link href="https://fonts.googleapis.com/css2?family=Orbitron:wght@600;700&family=Exo+2:wght@400;600&display=swap" rel="stylesheet">
<style>
  :root {
    --lime: #93d43b;
    --lime-light: #b4ea5c;
    --lime-dark: #6fa82a;
    --teal: #2c5461;
    --teal-deep: #1d3a44;
    --ink: #18262c;
    --ink-teal: #24606f;
    --paper-white: #eef3ea;
    --stage: #1f1f21;
  }
  * { box-sizing: border-box; margin: 0; padding: 0; }
  html, body {
    width: 1200px; height: 900px; overflow: hidden;
    background: var(--stage);
  }
  .canvas { position: relative; width: 1200px; height: 900px; }

  .card {
    position: absolute;
    width: 540px; height: 309px;
    border-radius: 3px;
    overflow: hidden;
    box-shadow: 0 14px 30px rgba(0,0,0,.45);
  }

  /* Front */
  .card--front {
    left: 400px; top: 90px;
    background: radial-gradient(ellipse at 50% 40%, var(--lime-light), var(--lime) 60%, var(--lime-dark));
    display: flex; flex-direction: column; align-items: center; justify-content: center;
  }
  .brand-dot {
    width: 74px; height: 74px; border-radius: 50%;
    background: var(--ink);
    margin-bottom: 16px;
  }
  .brand-name {
    font-family: "Orbitron", sans-serif;
    font-weight: 700;
    font-size: 34px;
    letter-spacing: 1px;
    color: var(--ink);
  }
  .tagline {
    margin-top: 8px;
    font-family: "Exo 2", sans-serif;
    font-weight: 600;
    font-size: 14px;
    letter-spacing: 2px;
    color: var(--ink-teal);
  }

  /* Back */
  .card--back {
    left: 280px; top: 480px;
    background: var(--lime);
    padding: 14px;
  }
  .back-panel {
    position: relative; width: 100%; height: 100%;
    background: linear-gradient(160deg, var(--teal) 0%, var(--teal-deep) 100%);
  }
  .tower-scene {
    position: absolute; right: 40px; top: 0;
    width: 200px; height: 210px;
    border-radius: 0 0 90px 90px;
    background: radial-gradient(circle at 50% 30%, var(--lime-light) 0%, var(--lime) 45%, var(--teal-deep) 100%);
  }
  .contact {
    position: absolute; left: 22px; top: 62px;
    font-family: "Exo 2", sans-serif;
    color: var(--paper-white);
  }
  .contact__name {
    font-family: "Orbitron", sans-serif;
    font-weight: 600;
    font-size: 22px;
    color: var(--lime);
    letter-spacing: 1px;
  }
  .contact__title {
    font-size: 11px; letter-spacing: 1.5px;
    text-transform: uppercase; margin-bottom: 18px;
  }
  .contact__line { font-size: 12px; letter-spacing: 1px; line-height: 17px; text-transform: uppercase; }
  .contact__label { color: var(--lime); margin-right: 4px; }
  .contact__gap { margin-left: 12px; }
  .back-brand {
    position: absolute; left: 26px; bottom: 22px;
    font-family: "Orbitron", sans-serif;
    font-weight: 700; font-size: 26px;
    color: var(--lime);
    letter-spacing: 1px;
  }
  .social {
    position: absolute; right: 10px; top: 120px;
    display: flex; flex-direction: column; gap: 4px;
  }
  .social span { width: 9px; height: 9px; background: var(--lime); display: block; }
</style>
</head>
<body>
<main class="canvas">
  <section class="card card--front" aria-label="Card front">
    <div class="brand-dot" aria-hidden="true"></div>
    <h1 class="brand-name">Ascend Kingdoms</h1>
    <p class="tagline">RAISING THE BAR OF PLAY</p>
  </section>

  <section class="card card--back" aria-label="Card back">
    <div class="back-panel">
      <div class="tower-scene" role="img" aria-label="Castle tower silhouette with birds in front of a glowing green moon"></div>
      <div class="contact">
        <h2 class="contact__name">MARCUS HALE</h2>
        <p class="contact__title">Producer and Designer</p>
        <p class="contact__line"><span class="contact__label">P:</span>555014820<span class="contact__gap"><span class="contact__label">F:</span>555014821</span></p>
        <p class="contact__line"><span class="contact__label">E:</span>info@ascendkingdoms.com</p>
        <p class="contact__line">www.ascendkingdoms.com</p>
      </div>
      <div class="social" aria-hidden="true"><span></span><span></span><span></span></div>
      <p class="back-brand">Ascend Kingdoms</p>
    </div>
  </section>
</main>
</body>
</html>
```